Media and Film Company Needs a New Website

We produce highly stylized commercials and film pieces for our clients. We also produce live events, both corporate and theatrical. Looking for a site that can show off our client videos - have a polished way to show off our team, and be able to create pages to highlight our clients and give a full overview of our project/process with them. We design simple website for some of our clients - so we are very wordpress familiar, and would like something that doesn't feel like a template.

Target Market(s)

content creators, creative directors, production teams, marketing agencies

Industry/Entity Type

Film Production

Number of Pages Required

4 page

Font styles to use
Sans Serif

Requirements
Must have
• slick looking video embed (from YT or Vimeo)
• project pages - client snapshot (what we did for them, how we did it)
• nice landing page, have our company video reel on the page
• testimonials
• contact page
• ability to have photos as a background if we want
Nice to have
• polished clean look - look to our logo colors and linear elements
• we produce very stylized videos for our clients and our website should reflect that
Should not have
• template look or feel to it- please bring your flare to the project!
• take a look at our current site - zantorvo.com we need a better way to highlight our work and our clients

```html
<!DOCTYPE html>
<html lang="en">
<head>
<meta charset="utf-8">
<title>Zantorvo Media &amp; Entertainment</title>
<link href="https://fonts.googleapis.com/css2?family=Exo+2:wght@400;600;700&family=Open+Sans:wght@400;600&display=swap" rel="stylesheet">
<style>
:root{
  --gold:#c9a227;
  --gold-dark:#a9861c;
  --ink:#161616;
  --charcoal:#1e1e1e;
  --paper:#ffffff;
  --mist:#f3f3f3;
  --blue:#2a8bd0;
  --text:#3a3a3a;
  --muted:#7a7a7a;
}
*{box-sizing:border-box;margin:0;padding:0}
html,body{width:1200px;height:3600px;overflow:hidden}
body{font-family:"Open Sans",Arial,sans-serif;color:var(--text);background:var(--paper)}
.section-title{font-family:"Exo 2",Arial,sans-serif;font-weight:700;font-size:38px;letter-spacing:3px;text-align:center;color:var(--ink)}
.btn{display:inline-block;background:var(--gold);color:#fff;font-family:"Exo 2",sans-serif;font-weight:700;font-size:16px;letter-spacing:1.5px;padding:14px 34px;text-transform:uppercase}

/* Hero */
.hero{position:relative;height:650px;overflow:hidden}
.hero-photo{position:absolute;inset:0;background:
  radial-gradient(ellipse at 50% 85%,#2a3540 0%,rgba(30,40,50,0) 45%),
  linear-gradient(180deg,#2f3d66 0%,#55709b 35%,#8ea3be 55%,#3b4a57 78%,#1b2229 100%)}
.brand{position:absolute;top:200px;left:0;right:0;text-align:center;color:#fff;font-family:"Exo 2",sans-serif;font-weight:700}
.brand-name{font-size:96px;letter-spacing:4px;line-height:1}
.brand-sub{font-size:30px;letter-spacing:3px;margin-top:8px}
.main-nav{position:absolute;left:0;right:0;top:600px;height:50px;background:rgba(14,14,14,.85);display:flex;padding-left:30px}
.main-nav a{font-family:"Exo 2",sans-serif;font-weight:600;font-size:17px;color:#fff;text-decoration:none;padding:0 28px;line-height:50px;letter-spacing:1px}
.main-nav a.active{background:var(--gold)}
.main-nav .spacer{flex:1}

/* Services */
.services{height:480px;background:var(--mist);padding-top:65px}
.service-grid{display:grid;grid-template-columns:repeat(4,1fr);gap:30px;padding:60px 110px 0}
.service-icon{width:64px;height:56px;color:var(--blue)}
.service h3{font-family:"Exo 2",sans-serif;font-weight:700;font-size:20px;color:var(--blue);text-transform:uppercase;margin:14px 0 16px;line-height:1.2}
.service li{list-style:none;font-size:15px;line-height:26px;color:var(--text);position:relative;padding-left:16px}
.service li::before{content:"";position:absolute;left:0;top:11px;width:6px;height:6px;background:var(--blue)}

/* About */
.about{height:390px;position:relative;background:var(--paper)}
.about-copy{position:absolute;left:110px;top:70px;width:520px}
.about-copy h2{font-family:"Exo 2",sans-serif;font-weight:700;font-size:44px;color:var(--ink);margin-bottom:18px}
.about-copy p{font-size:15px;line-height:24px;margin-bottom:26px}
.about-photo{position:absolute;right:0;top:30px;width:520px;height:340px;background:linear-gradient(135deg,#3a3a3a,#9a9a9a 55%,#262626)}

/* Popular production */
.popular{height:865px;background:var(--charcoal);position:relative}
.popular .cam{position:absolute;left:565px;top:60px;width:70px;height:56px;color:#fff}
.popular .section-title{color:#fff;padding-top:130px}
.thumb-grid{position:absolute;top:220px;left:0;right:0;display:grid;grid-template-columns:repeat(4,1fr);column-gap:28px;row-gap:28px;padding:0 0}
.thumb{height:140px}
.popular .btn{position:absolute;top:760px;left:518px}

/* Portfolio */
.portfolio-head{height:95px;background:var(--paper);display:flex;align-items:center;justify-content:center;gap:16px}
.portfolio-head svg{width:52px;height:42px;color:var(--blue)}
.portfolio-strip{height:405px;background:var(--ink);position:relative}
.slide{position:absolute;top:30px;height:270px}
.slider-arrows{position:absolute;top:325px;left:0;right:0;display:flex;justify-content:center;gap:40px}
.slider-arrows svg{width:22px;height:34px}

/* Clients */
.clients{height:295px;background:var(--paper);position:relative;padding-top:55px}
.client-row{position:absolute;top:160px;left:90px;right:90px;display:flex;justify-content:space-between;align-items:center}
.client{font-family:"Open Sans",sans-serif;font-weight:600;font-size:18px;color:#4a4a4a;display:flex;align-items:center;gap:8px;letter-spacing:1px}
.client i{display:block;width:14px;height:14px;background:#b8b8b8}
.client-arrow{position:absolute;top:165px;width:34px;height:50px;background:#9a9a9a;display:flex;align-items:center;justify-content:center}
.client-arrow svg{width:12px;height:22px}

/* Footer */
.site-footer{height:420px;background:var(--ink);color:#fff;text-align:center;position:relative}
.footer-brand{position:absolute;top:80px;left:0;right:0;font-family:"Exo 2",sans-serif;font-weight:700}
.footer-brand .brand-name{font-size:56px}
.footer-brand .brand-sub{font-size:18px;margin-top:4px}
.follow{position:absolute;top:196px;left:0;right:0;font-family:"Exo 2",sans-serif;font-weight:600;font-size:18px;letter-spacing:2px}
.social{position:absolute;top:232px;left:0;right:0;display:flex;justify-content:center;gap:10px}
.social span{width:28px;height:28px;border-radius:50%;background:var(--gold)}
.footer-rule{position:absolute;top:290px;left:420px;width:360px;height:1px;background:#555}
.contact-line{position:absolute;top:318px;left:0;right:0;font-size:17px;display:flex;justify-content:center;align-items:center;gap:10px}
.contact-line svg{width:18px;height:18px;color:var(--gold)}
.copyright{position:absolute;top:368px;left:0;right:0;font-size:13px;color:#bbb;letter-spacing:1px}
</style>
</head>
<body>

<header class="hero">
  <div class="hero-photo" role="img" aria-label="Dusk photograph of a bronze monument against a cloudy blue sky"></div>
  <div class="brand">
    <div class="brand-name">ZANTORVO</div>
    <div class="brand-sub">&amp; ENTERTAINMENT</div>
  </div>
  <nav class="main-nav">
    <a class="active" href="#">HOME</a>
    <a href="#">PORTFOLIO</a>
    <a href="#">ABOUT US</a>
    <a href="#">TESTIMONIALS</a>
    <span class="spacer"></span>
    <a href="#">PRESS</a>
    <a href="#">CONTACT US</a>
  </nav>
</header>

<section class="services">
  <h2 class="section-title">WHAT WE DO</h2>
  <div class="service-grid">
    <div class="service">
      <svg class="service-icon" viewBox="0 0 64 56" fill="none" stroke="currentColor" stroke-width="3"><rect x="4" y="18" width="40" height="30" rx="3"/><path d="M44 28l16-8v26l-16-8"/><circle cx="14" cy="10" r="7"/><circle cx="32" cy="10" r="7"/></svg>
      <h3>Film &amp; Media<br>Production</h3>
      <ul><li>Lumacraft Creative Suite</li><li>Motion Graphics</li><li>4K Workflow</li><li>Direct to Web/Streamline</li></ul>
    </div>
    <div class="service">
      <svg class="service-icon" viewBox="0 0 64 56" fill="none" stroke="currentColor" stroke-width="3"><rect x="6" y="12" width="52" height="38" rx="4"/><path d="M22 4l10 8 10-8"/><text x="32" y="37" text-anchor="middle" font-family="Exo 2, sans-serif" font-size="14" font-weight="700" fill="currentColor" stroke="none">LIVE</text></svg>
      <h3>Live<br>Production</h3>
      <ul><li>Theatrical Producing</li><li>Production Management</li><li>Lighting &amp; Video Design</li><li>Audio System Design</li></ul>
    </div>
    <div class="service">
      <svg class="service-icon" viewBox="0 0 64 56" fill="none" stroke="currentColor" stroke-width="3"><rect x="8" y="4" width="36" height="48" rx="3"/><path d="M16 16h20M16 26h20M16 36h12"/><path d="M56 8l-14 34-4 8 1-9 13-34z"/></svg>
      <h3>PR, Marketing<br>&amp; Advertising</h3>
      <ul><li>Branding</li><li>Social Media</li><li>Media Relations &amp; Outreach</li><li>Street Teams</li></ul>
    </div>
    <div class="service">
      <svg class="service-icon" viewBox="0 0 64 56" fill="none" stroke="currentColor" stroke-width="3"><rect x="8" y="8" width="48" height="44" rx="3"/><path d="M8 20h48M20 2v12M44 2v12"/><path d="M18 30h6M30 30h6M42 30h6M18 40h6M30 40h6"/></svg>
      <h3>Events</h3>
      <ul><li>Event Production</li><li>Staffing &amp; Hiring</li><li>Manage RFPS</li><li>Sponsor Relations</li></ul>
    </div>
  </div>
</section>

<section class="about">
  <div class="about-copy">
    <h2>About Zantorvo</h2>
    <p>Zantorvo Media &amp; Entertainment provides full service campaigns in film and media production, live entertainment &amp; theatrical production, marketing &amp; advertising, and event management in the DC metro area. Founded in 2009, Zantorvo Media &amp; Entertainment has built a reputation working for clients including the Northbay Film Society, Crestline Leaders Forum, Halvard Music, Riverbend Community Partners, and Lanternfield Events.</p>
    <a class="btn" href="#">Read More</a>
  </div>
  <div class="about-photo" role="img" aria-label="Black and white photograph of a studio film set with lights and camera"></div>
</section>

<section class="popular">
  <svg class="cam" viewBox="0 0 70 56" fill="none" stroke="currentColor" stroke-width="3"><circle cx="16" cy="12" r="9"/><circle cx="38" cy="12" r="9"/><rect x="4" y="24" width="44" height="28" rx="3"/><path d="M48 32l18-8v26l-18-8"/></svg>
  <h2 class="section-title">MOST POPULAR PRODUCTION</h2>
  <div class="thumb-grid">
    <div class="thumb" role="img" aria-label="Video still: gold title card for an event promo" style="background:linear-gradient(135deg,#7a6420,#c9a227)"></div>
    <div class="thumb" role="img" aria-label="Video still: community organisation logo on a wall" style="background:linear-gradient(135deg,#6a5a4a,#b59a80)"></div>
    <div class="thumb" role="img" aria-label="Video still: brick building with green lawn" style="background:linear-gradient(180deg,#8fb0d0,#6c8a4a)"></div>
    <div class="thumb" role="img" aria-label="Video still: interview subject on blue background" style="background:linear-gradient(135deg,#1f3e7a,#3a6ab0)"></div>
    <div class="thumb" role="img" aria-label="Video still: interview in warm indoor light" style="background:linear-gradient(135deg,#8a4a30,#d89a6a)"></div>
    <div class="thumb" role="img" aria-label="Video still: interview in a wood panelled room" style="background:linear-gradient(135deg,#4a3220,#9a7050)"></div>
    <div class="thumb" role="img" aria-label="Video still: outdoor interview on a green field" style="background:linear-gradient(135deg,#3e6a30,#8ab060)"></div>
    <div class="thumb" role="img" aria-label="Video still: bright red and white show title card" style="background:linear-gradient(135deg,#c43a2a,#f0d0c0)"></div>
    <div class="thumb" role="img" aria-label="Video still: interview against a white wall" style="background:linear-gradient(135deg,#d8d8d8,#a07060)"></div>
    <div class="thumb" role="img" aria-label="Video still: interview in a dim room" style="background:linear-gradient(135deg,#2a2a2a,#6a5a50)"></div>
    <div class="thumb" role="img" aria-label="Video still: car commercial on a dark background" style="background:linear-gradient(135deg,#0a0a0a,#444)"></div>
    <div class="thumb" role="img" aria-label="Video still: theatre production poster in red and black" style="background:linear-gradient(135deg,#1a1a1a,#9a2a20)"></div>
  </div>
  <a class="btn" href="#">Load More</a>
</section>

<section class="portfolio-head">
  <svg viewBox="0 0 52 42" fill="currentColor"><path d="M2 6h18l4 5h24v6H10L2 38z"/><path d="M10 19h40l-8 21H2z"/></svg>
  <h2 class="section-title">OUR PORTFOLIO</h2>
</section>

<section class="portfolio-strip">
  <div class="slide" role="img" aria-label="Photograph of a festival audience under red stage light" style="left:0;width:380px;background:linear-gradient(160deg,#3a1a3a,#a0303a 60%,#1a1a2a)"></div>
  <div class="slide" role="img" aria-label="Photograph of a speaker at a podium on a blue stage" style="left:410px;width:380px;background:linear-gradient(160deg,#1a3a7a,#4a7ac0 50%,#1a1a1a)"></div>
  <div class="slide" role="img" aria-label="Photograph of guests posing at an indoor reception" style="left:820px;width:380px;background:linear-gradient(160deg,#5a4a40,#c0a080 55%,#3a2a20)"></div>
  <div class="slider-arrows">
    <svg viewBox="0 0 22 34" fill="none" stroke="#fff" stroke-width="4"><path d="M18 3L5 17l13 14"/></svg>
    <svg viewBox="0 0 22 34" fill="none" stroke="#fff" stroke-width="4"><path d="M4 3l13 14L4 31"/></svg>
  </div>
</section>

<section class="clients">
  <h2 class="section-title">OUR CLIENTS</h2>
  <a class="client-arrow" href="#" style="left:0"><svg viewBox="0 0 12 22" fill="none" stroke="#fff" stroke-width="3"><path d="M10 2L2 11l8 9"/></svg></a>
  <div class="client-row">
    <span class="client"><i></i>RIVERBEND</span>
    <span class="client"><i></i>NORTHBAY</span>
    <span class="client"><i></i>CRESTLINE</span>
    <span class="client"><i></i>KETTLEWORKS</span>
    <span class="client"><i></i>HALVARD</span>
    <span class="client"><i></i>FORGELINE</span>
  </div>
  <a class="client-arrow" href="#" style="right:0"><svg viewBox="0 0 12 22" fill="none" stroke="#fff" stroke-width="3"><path d="M2 2l8 9-8 9"/></svg></a>
</section>

<footer class="site-footer">
  <div class="footer-brand">
    <div class="brand-name">ZANTORVO</div>
    <div class="brand-sub">&amp; ENTERTAINMENT</div>
  </div>
  <div class="follow">FOLLOW US</div>
  <div class="social"><span></span><span></span><span></span><span></span><span></span><span></span><span></span></div>
  <div class="footer-rule"></div>
  <div class="contact-line">
    <svg viewBox="0 0 18 18" fill="currentColor"><path d="M4 1l3 4-2 2c1 2 3 4 5 5l2-2 4 3-2 4C7 17 1 11 0 4z"/></svg>
    <span>Contact us today – info@zantorvo.com</span>
  </div>
  <div class="copyright">©2017 ZANTORVO MEDIA &amp; ENTERTAINMENT</div>
</footer>

</body>
</html>
```